Wedding Day Custom Wine Label - Tasmanian (Tamar Valley) wine

I am looking for a custom design that will be put on a wine label to commemorate a very good friend's wedding day.

We will need to be able to take the design and print it on to sticker labels that we can put on to wine bottles.

The bride and groom have asked for a simplistic label design (see example image attached). We need two labels. One for "Pinot Noir" wine and the other for "Chardonnay" wine. We would like the label to say:

The Hartwell's
Pinot Noir
2023
Tamar Valley

and for for the other wine variety:

The Hartwell's
Chardonnay
2023
Tamar Valley

smaller text below to say:

13.5% ALC/VOL 750ML
MEGAN & LIAM - 31.10.2024

I am happy to consider other variations - the bride & groom would prefer something minimalistic. Elegant and classy.

Target Market(s)

the bride & groom

Requirements
Must have
• Wedding date (31.10.2024). Wine type (Pinot Noir or Chardonnay).
Should not have
• images not essential

```html
<!DOCTYPE html>
<html lang="en">
<head>
<meta charset="utf-8">
<title>The Hartwell's Chardonnay – Wedding Wine Label</title>
<link rel="stylesheet" href="https://fonts.googleapis.com/css2?family=Arimo:wght@400&family=Marcellus&family=Pinyon+Script&display=swap">
<style>
  :root {
    --backdrop: #63112a;
    --label-navy: #1b1e3a;
    --label-navy-deep: #12132a;
    --label-navy-glow: #242a55;
    --gold-light: #e9d6a2;
    --gold: #b8975a;
    --gold-dark: #7a5f2e;
    --silver-light: #f2f2f2;
    --silver: #a9a9ae;
    --ink-dark: #1a1a1a;
    --text-white: #f4f4f4;
    --text-soft: #d8d8dc;
  }
  * { margin: 0; padding: 0; box-sizing: border-box; }
  html, body {
    width: 1000px;
    height: 1200px;
    overflow: hidden;
    background: var(--backdrop);
  }
  .canvas {
    position: relative;
    width: 1000px;
    height: 1200px;
    background: var(--backdrop);
  }
  .wine-label {
    position: absolute;
    left: 124px;
    top: 144px;
    width: 752px;
    height: 912px;
    display: block;
    box-shadow: 0 18px 40px rgba(0, 0, 0, 0.35);
  }
  .script-the { font-family: "Pinyon Script", cursive; }
  .family-name { font-family: "Marcellus", serif; }
  .sans-text { font-family: "Arimo", sans-serif; }
</style>
</head>
<body>
<main class="canvas">
  <svg class="wine-label" viewBox="0 0 470 570" xmlns="http://www.w3.org/2000/svg" aria-label="The Hartwell's Chardonnay 2023 wedding wine label">
    <defs>
      <radialGradient id="label-ground" cx="50%" cy="50%" r="70%">
        <stop offset="0%" stop-color="var(--label-navy-glow)"/>
        <stop offset="60%" stop-color="var(--label-navy)"/>
        <stop offset="100%" stop-color="var(--label-navy-deep)"/>
      </radialGradient>
      <linearGradient id="frame-gold" x1="0" y1="0" x2="1" y2="1">
        <stop offset="0%" stop-color="var(--gold)"/>
        <stop offset="35%" stop-color="var(--gold-light)"/>
        <stop offset="55%" stop-color="#8c2a2a"/>
        <stop offset="75%" stop-color="var(--gold-light)"/>
        <stop offset="100%" stop-color="var(--gold-dark)"/>
      </linearGradient>
      <linearGradient id="band-gold" x1="0" y1="0" x2="1" y2="0">
        <stop offset="0%" stop-color="var(--gold-dark)"/>
        <stop offset="25%" stop-color="var(--gold)"/>
        <stop offset="50%" stop-color="var(--gold-light)"/>
        <stop offset="75%" stop-color="var(--gold)"/>
        <stop offset="100%" stop-color="var(--gold-dark)"/>
      </linearGradient>
      <linearGradient id="name-silver" x1="0" y1="0" x2="0" y2="1">
        <stop offset="0%" stop-color="var(--silver-light)"/>
        <stop offset="55%" stop-color="var(--silver)"/>
        <stop offset="100%" stop-color="var(--silver-light)"/>
      </linearGradient>
    </defs>

    <!-- label ground -->
    <rect class="label-ground" x="0" y="0" width="470" height="570" fill="url(#label-ground)"/>

    <!-- corner flourishes -->
    <g role="img" aria-label="Gold floral flourish, top left corner">
      <rect x="12" y="22" width="62" height="48" rx="10" fill="var(--gold)" opacity="0.12"/>
    </g>
    <g role="img" aria-label="Silver leafy sprig, left side">
      <rect x="4" y="128" width="60" height="34" rx="10" fill="var(--silver)" opacity="0.1"/>
    </g>
    <g role="img" aria-label="Silver leafy sprig, right side">
      <rect x="420" y="130" width="40" height="26" rx="8" fill="var(--silver)" opacity="0.1"/>
    </g>
    <g role="img" aria-label="Gold floral flourish, bottom left corner">
      <rect x="12" y="488" width="72" height="60" rx="10" fill="var(--gold)" opacity="0.12"/>
    </g>

    <!-- arched frame -->
    <path class="label-frame"
          d="M25 96 Q25 88 33 88 L78 88
             C110 50 150 22 235 22
             C320 22 360 50 392 88 L470 88
             M25 96 L25 474 Q25 482 33 482 L78 482
             C110 522 150 550 235 550
             C320 550 360 522 392 482 L470 482"
          fill="none" stroke="url(#frame-gold)" stroke-width="1.6"/>

    <!-- heading -->
    <text class="script-the" x="235" y="136" text-anchor="middle" font-size="26" fill="var(--text-white)">The</text>
    <text class="family-name" x="237" y="202" text-anchor="middle" font-size="52" fill="url(#name-silver)" textLength="310" lengthAdjust="spacingAndGlyphs">HARTWELL'S</text>

    <!-- variety band -->
    <rect class="variety-band" x="77" y="212" width="306" height="43" fill="url(#band-gold)"/>
    <text class="sans-text" x="230" y="248" text-anchor="middle" font-size="37" fill="var(--ink-dark)" textLength="296" lengthAdjust="spacingAndGlyphs">CHARDONNAY</text>

    <!-- details -->
    <text class="sans-text" x="235" y="287" text-anchor="middle" font-size="26" fill="var(--text-white)">2023</text>
    <text class="sans-text" x="230" y="354" text-anchor="middle" font-size="24" fill="var(--text-white)">Tamar Valley</text>
    <text class="sans-text" x="226" y="396" text-anchor="middle" font-size="17" fill="var(--text-soft)">13.5% ALC/VOL 750ML</text>
    <text class="sans-text" x="230" y="464" text-anchor="middle" font-size="18" fill="var(--text-soft)">MEGAN &amp; LIAM - 31.10.2024</text>
  </svg>
</main>
</body>
</html>
```